Business Card for a Jewellery Brand

Business card for an upscale jewellery brand. Attached is the brand logo and icon and color board. I am looking for two card versions: one for the founder and one is generic. The card should be elegant and convey upscale and premium feel. I am open to both square and rectangle card shapes.

Industry/Entity Type

Jewelry

Contact Information for Business Card

Two cards: (1) Sunila Perumbadi (Founder) (2) General
(1) Sunila Perumbadi card should have Name: Sunila Perumbadi, Title: Founder Email id: sunila@quelm.com.au. Phone no: +61412555307
(2) Generic card should have Email id: info@quelm.com.au. Phone no: +61431555962

Requirements
Must have
• Workmark
• ICON
• Phone no
• Email ID
• ABN: 48917205563 (Note: ABN is Business number in Australia)
• Website: www.quelm.com.au
• Instagram: quelm_jewellery
• Facebook: @quelmjewellery
Nice to have
• Tagline

```html
<!DOCTYPE html>
<html lang="en">
<head>
<meta charset="utf-8">
<title>QUELM Business Cards</title>
<link href="https://fonts.googleapis.com/css2?family=Lato:wght@300;400;700&display=swap" rel="stylesheet">
<style>
  :root {
    --backdrop: #e4e4df;
    --card: #1d1c1e;
    --silver: #c8c1b2;
    --silver-dim: #8f8a80;
    --rose: #e6a19d;
    --rose-dim: #c98784;
  }
  html, body {
    margin: 0;
    padding: 0;
    width: 1200px;
    height: 1200px;
    overflow: hidden;
    background: var(--backdrop);
    font-family: "Lato", Arial, sans-serif;
  }
  .canvas {
    width: 1200px;
    height: 1200px;
    display: flex;
    flex-direction: column;
    align-items: center;
    justify-content: center;
    gap: 40px;
  }
  .card {
    position: relative;
    width: 880px;
    height: 538px;
    background: var(--card);
    box-shadow: 0 14px 30px rgba(0,0,0,0.18);
    box-sizing: border-box;
  }

  /* Front */
  .card-front {
    display: flex;
    flex-direction: column;
    align-items: center;
    justify-content: center;
  }
  .brand-lockup {
    display: flex;
    flex-direction: column;
    align-items: center;
  }
  .brand-mark {
    width: 34px;
    height: 34px;
    border: 3px solid var(--silver);
    box-sizing: border-box;
    margin-bottom: 30px;
  }
  .brand-name {
    font-weight: 300;
    font-size: 84px;
    letter-spacing: 26px;
    margin-right: -26px;
    color: var(--silver);
    line-height: 1;
  }
  .tagline {
    margin-top: 14px;
    font-weight: 400;
    font-size: 22px;
    letter-spacing: 2.5px;
    color: var(--silver-dim);
    text-transform: uppercase;
  }

  /* Back */
  .card-back .brand-name {
    position: absolute;
    top: 62px;
    right: 70px;
    font-size: 64px;
    letter-spacing: 20px;
    margin-right: -20px;
    color: var(--rose);
  }
  .contact-person {
    position: absolute;
    left: 60px;
    top: 224px;
    padding-left: 22px;
    border-left: 7px solid var(--rose);
  }
  .person-name {
    font-size: 32px;
    color: var(--rose);
    line-height: 1.15;
  }
  .person-name strong { font-weight: 700; }
  .person-title {
    font-size: 20px;
    color: var(--rose-dim);
  }
  .contact-list {
    position: absolute;
    left: 88px;
    top: 330px;
    margin: 0;
    padding: 0;
    list-style: none;
    font-size: 21px;
    color: var(--rose-dim);
    line-height: 33px;
  }
  .contact-list li {
    display: flex;
    align-items: center;
    gap: 12px;
  }
  .contact-list .abn { margin-bottom: 14px; }
  .contact-icon {
    width: 18px;
    height: 18px;
    flex: none;
  }
  .social-spot {
    width: 16px;
    height: 16px;
    background: var(--rose-dim);
    border-radius: 2px;
    flex: none;
    margin: 0 1px;
  }
  .website {
    position: absolute;
    right: 70px;
    bottom: 104px;
    font-size: 21px;
    color: var(--rose-dim);
  }
</style>
</head>
<body>
<main class="canvas">
  <section class="card card-front" aria-label="Card front">
    <div class="brand-lockup">
      <span class="brand-mark"></span>
      <span class="brand-name">QUELM</span>
      <span class="tagline">Exquisite Silver Jewellery</span>
    </div>
  </section>

  <section class="card card-back" aria-label="Card back">
    <span class="brand-name">QUELM</span>
    <div class="contact-person">
      <div class="person-name">Sunila <strong>Perumbadi</strong></div>
      <div class="person-title">Founder</div>
    </div>
    <ul class="contact-list">
      <li class="abn">ABN: 48917205563</li>
      <li>
        <svg class="contact-icon" viewBox="0 0 18 18" aria-hidden="true">
          <rect x="1" y="4" width="16" height="11" fill="#c98784"/>
          <path d="M1 4 L9 10 L17 4" fill="none" stroke="#1d1c1e" stroke-width="1.5"/>
        </svg>
        sunila@quelm.com.au
      </li>
      <li>
        <svg class="contact-icon" viewBox="0 0 18 18" aria-hidden="true">
          <path d="M1 7 Q9 1 17 7 L15 9 L12 7.5 L12 6 Q9 5 6 6 L6 7.5 L3 9 Z" fill="#c98784"/>
          <rect x="4" y="10" width="10" height="6" rx="1" fill="#c98784"/>
        </svg>
        +61412555307
      </li>
      <li><span class="social-spot"></span>quelm_jewellery</li>
      <li><span class="social-spot"></span>@quelmjewellery</li>
    </ul>
    <span class="website">www.quelm.com.au</span>
  </section>
</main>
</body>
</html>
```